South Carolina Bridal and Formal Wear Store

We want The Gown Parlor of Marlowe website to feel luxurious, elegant, welcoming, and approachable—without feeling overpriced or intimidating. The site should immediately show that we are a full-service bridal and formal wear destination, offering bridal gowns, prom, mothers’ dresses, tuxedos and suits, accessories, and more. We want beautiful, high-end imagery and a clean, modern design while still reflecting the warm, personal experience customers receive when they walk into our boutique. Most importantly, the website should be easy to shop and navigate, allowing customers to browse our collections, see what we offer, understand price ranges, book appointments, and feel excited and comfortable choosing The Gown Parlor of Marlowe for all of their special-event needs.

Target Market(s)

Women ages 18-50. Brides, engaged women, mothers of the occasion

Industry/Entity Type

Bridal and Formal Wear

Coding

Coded - Design and coding required

Number of Pages Required

5+ page

Font styles to use
Sans Serif

Colors

Designer to choose colors to be used in the design.

Requirements
Must have
• Appointment area, about us staff area, what we offer and designers our logo
Nice to have
• Modern Southern Luxury: Clean, elegant, and upscale with soft neutral tones, beautiful bridal photography, and a warm Lowcountry feel.
Should not have
• pricing

```html
<!DOCTYPE html>
<html lang="en">
<head>
<meta charset="utf-8">
<title>The Gown Parlor of Marlowe</title>
<link rel="stylesheet" href="https://fonts.googleapis.com/css2?family=Cormorant+Garamond:wght@300;400&family=Pinyon+Script&family=Manrope:wght@300;400;500&display=swap">
<style>
:root{
  --cream:#f7f3ef;
  --ink:#3b2f28;
  --soft:#7a6c62;
  --line:#cfc5bb;
  --taupe:#b5a494;
  --sand:#e8ddd0;
  --white:#ffffff;
  --accent:#8a6d55;
}
*{margin:0;padding:0;box-sizing:border-box}
html,body{width:1200px;height:4010px;overflow:hidden;background:var(--cream)}
body{position:relative;font-family:"Manrope",sans-serif;color:var(--ink);font-weight:300}
.abs{position:absolute}
.serif{font-family:"Cormorant Garamond",serif;font-weight:300}
.script{font-family:"Pinyon Script",cursive}
.photo{position:absolute}
.link{font-size:11px;letter-spacing:1.2px;font-weight:500;text-transform:uppercase;color:var(--ink);border-bottom:1px solid var(--accent);padding-bottom:3px;text-decoration:none}

.hero{position:absolute;left:0;top:0;width:1200px;height:584px;background:linear-gradient(100deg,#3a2a20 0%,#5c4637 35%,#8a7462 55%,#4a3729 80%,#2e2119 100%)}
.hero .kicker{left:95px;top:70px;font-size:11px;letter-spacing:2px;color:#e9dfd5}
.hero h1{position:absolute;left:93px;top:95px;font-size:66px;line-height:62px;color:var(--white);font-weight:300;letter-spacing:1px}
.hero .count{left:95px;top:448px;color:#fff;display:flex;align-items:center;gap:10px}
.hero .count b{font-family:"Cormorant Garamond",serif;font-weight:300;font-size:34px}
.hero .count span{font-size:13px;color:#d8ccc0}
.hero .tag{left:789px;top:430px;width:250px;font-size:15px;line-height:23px;color:#f3ece5}

.nav{position:absolute;left:0;top:584px;width:1200px;height:62px;border-bottom:1px solid var(--line);background:var(--cream)}
.nav ul{position:absolute;left:83px;top:23px;display:flex;gap:30px;list-style:none;font-size:11.5px;letter-spacing:1.2px}
.brand{position:absolute;text-align:center;color:var(--ink)}
.brand .name{font-family:"Cormorant Garamond",serif;font-weight:400;display:block;line-height:1}
.brand .sub{display:block;font-family:"Manrope",sans-serif;font-weight:300}
.nav .brand{left:500px;top:11px;width:200px}
.nav .brand .name{font-size:22px}
.nav .brand .sub{font-size:8px;letter-spacing:3px;margin-top:3px}
.nav .cta{right:83px;top:22px}

.story .script{top:748px;left:0;width:1200px;text-align:center;font-size:18px;color:var(--soft)}
.story h2{position:absolute;top:780px;left:0;width:1200px;text-align:center;font-size:70px;line-height:68px;font-weight:300}
.story p{position:absolute;left:365px;top:944px;width:470px;text-align:center;font-size:13px;line-height:23px;color:var(--soft)}
.story .link{left:534px;top:1077px}

.marquee{position:absolute;left:0;top:1296px;width:1200px;height:67px;border-top:1px solid var(--line);border-bottom:1px solid var(--line)}
.marquee span{position:absolute;top:24px;font-size:15px;letter-spacing:5px;color:var(--ink);white-space:nowrap}

.services .script{top:1445px;left:0;width:1200px;text-align:center;font-size:17px;color:var(--soft)}
.services h2{position:absolute;top:1470px;left:0;width:1200px;text-align:center;font-size:72px;font-weight:300}
.arrows{left:78px;top:2050px;display:flex;gap:10px}
.card-title{left:0;width:1200px;text-align:center}
.services .t1{top:2096px;font-size:30px}
.services .t2{top:2135px;font-size:13px;color:var(--soft)}
.services .link{left:549px;top:2175px}

.appts{position:absolute;left:0;top:2287px;width:1200px;height:601px;background:var(--taupe);overflow:hidden}
.appts .divider{left:600px;top:0;width:1px;height:601px;background:#9f8e7f}
.appt{position:absolute;top:0;width:600px;text-align:center;color:var(--white)}
.appt h3{margin-top:79px;font-size:38px;font-weight:300;letter-spacing:.5px}
.appt p{margin:30px auto 0;width:420px;font-size:13px;line-height:23px;color:#f4eee8}
.appt .btn{display:inline-block;margin-top:55px;padding:10px 20px;border:1px solid #8f7e6f;font-size:11.5px;letter-spacing:1.2px;font-weight:500;color:var(--ink)}

.faq{position:absolute;left:0;top:2888px;width:1200px;height:500px;background:var(--sand)}
.faq h2{position:absolute;left:82px;top:85px;font-size:52px;font-weight:300}
.faq ul{position:absolute;left:641px;top:84px;width:475px;list-style:none;border-top:1px solid var(--accent)}
.faq li{height:60px;border-bottom:1px solid var(--accent);display:flex;justify-content:space-between;align-items:center;font-size:15px;color:var(--ink)}
.faq li em{font-style:normal;font-size:16px;color:var(--soft)}
.faq .more{left:641px;top:406px;font-size:12px;color:var(--soft)}

.designers{position:absolute;left:0;top:3388px;width:1200px;height:132px;border-bottom:1px solid var(--line);display:flex;justify-content:center;align-items:center;gap:90px}
.designers span{font-family:"Cormorant Garamond",serif;font-weight:400;font-size:28px;color:var(--ink);display:flex;align-items:center;gap:10px}
.designers i{display:inline-block;width:14px;height:14px;background:var(--ink)}

.foot-top{position:absolute;left:0;top:3520px;width:1200px;height:70px;border-bottom:1px solid var(--line)}
.foot-top .link{position:absolute;left:83px;top:28px}
.foot-top .back{position:absolute;right:83px;top:28px;font-size:12px;letter-spacing:.5px}
.contact{left:83px;top:3618px;font-size:13px;line-height:29px}
.social{left:83px;top:3728px;font-size:12px}
.footer-brand{left:440px;top:3650px;width:320px}
.footer-brand .name{font-size:44px}
.footer-brand .sub{margin-top:4px;font-size:13px;letter-spacing:5px}
.address{left:893px;top:3618px;font-size:13px;line-height:19px}
.hours{left:893px;top:3680px;font-size:13px;line-height:22px}
.hours b{font-weight:500;letter-spacing:.8px;font-size:12px}
.bottom{position:absolute;left:0;top:3963px;width:1200px;border-top:1px solid var(--line)}
.bottom span{position:absolute;top:20px;font-size:9px;color:var(--soft)}
</style>
</head>
<body>

<section class="hero" role="img" aria-label="Bride in a corseted white gown leaning in an ornate antique doorway">
  <div class="abs kicker">Devoted to the art of bridal</div>
  <h1 class="serif">GOWN PARLOR<br>OF MARLOWE</h1>
  <div class="abs count"><b>01</b><span>/ 03</span>
    <svg width="30" height="10" viewBox="0 0 30 10"><path d="M0 5H28M23 1l5 4-5 4" stroke="#fff" fill="none" stroke-width="1"/></svg>
  </div>
  <p class="abs tag">We don't just help you find a dress — we create an experience that becomes part of your love story.</p>
</section>

<nav class="nav">
  <ul><li>ABOUT</li><li>SERVICES</li><li>FAQS</li><li>CONTACT</li></ul>
  <div class="brand"><span class="name">The Gown Parlor</span><span class="sub">OF MARLOWE</span></div>
  <a class="abs link cta">REQUEST AN APPOINTMENT</a>
</nav>

<section class="story">
  <div class="photo" style="left:924px;top:697px;width:226px;height:224px;background:linear-gradient(160deg,#2b2624,#4a3f39 60%,#1f1b19)" role="img" aria-label="Boutique staff group portrait in black outfits"></div>
  <div class="photo" style="left:0;top:906px;width:308px;height:306px;background:linear-gradient(180deg,#8e8a84,#b8aa98 50%,#6e5c4c)" role="img" aria-label="Staff smiling in front of the boutique storefront sign"></div>
  <div class="abs script">Experience that becomes part of your love story</div>
  <h2 class="serif">THE STORY OF<br>GOWN PARLOR</h2>
  <p>At The Gown Parlor of Marlowe, we don't just help you find a dress — we create an experience that becomes part of your love story. Every bride leaves feeling confident, radiant, and ready for her perfect day.</p>
  <a class="abs link">EXPLORE OUR STORY</a>
</section>

<div class="marquee">
  <span style="left:0">RMALWEAR •</span>
  <span style="left:222px">• BRIDAL •</span>
  <span style="left:420px">• TUXEDOS •</span>
  <span style="left:643px">• PROM •</span>
  <span style="left:822px">• ACCESSORIES •</span>
  <span style="left:1100px">• MOTHE</span>
</div>

<section class="services">
  <div class="abs script">Experience that becomes part of your love story</div>
  <h2 class="serif">SERVICES WE PROVIDE</h2>
  <div class="photo" style="left:82px;top:1637px;width:326px;height:391px;background:linear-gradient(160deg,#5a5a5a,#1c1c1c 55%,#3a3a3a)" role="img" aria-label="Groom in a black tuxedo"></div>
  <div class="photo" style="left:437px;top:1595px;width:326px;height:474px;background:linear-gradient(180deg,#2a2624 0%,#e9e6e1 40%,#f4f1ec 70%,#a8705c 100%)" role="img" aria-label="Bride in an off-shoulder white gown on brick steps"></div>
  <div class="photo" style="left:790px;top:1637px;width:326px;height:391px;background:linear-gradient(180deg,#dfe0da,#c9b49a 55%,#a98f74)" role="img" aria-label="Bride and bridesmaids in beaded champagne dresses cheering"></div>
  <div class="photo" style="left:985px;top:1930px;width:195px;height:195px;border-radius:50%;background:radial-gradient(circle,rgba(122,108,98,.14),rgba(122,108,98,0) 70%)" role="img" aria-label="Fine line floral sketch"></div>
  <div class="abs arrows">
    <svg width="12" height="16" viewBox="0 0 12 16"><path d="M9 2 3 8l6 6" stroke="#9a8f86" fill="none" stroke-width="1.3"/></svg>
    <svg width="12" height="16" viewBox="0 0 12 16"><path d="M3 2l6 6-6 6" stroke="#3b2f28" fill="none" stroke-width="1.3"/></svg>
  </div>
  <div class="abs card-title serif t1" style="font-weight:400">Bridal</div>
  <div class="abs card-title t2">Timeless elegance for the modern bride.</div>
  <a class="abs link">EXPLORE BRIDAL</a>
</section>

<section class="appts">
  <div class="abs divider"></div>
  <div class="appt" style="left:0">
    <h3 class="serif">VIP BRIDAL APPOINTMENT</h3>
    <p>Enjoy a fully private 2-hour VIP bridal appointment with exclusive access to our entire boutique and two dedicated bridal consultants assisting you throughout your visit.</p>
    <span class="btn">EXPLORE PACKAGE</span>
  </div>
  <div class="appt" style="left:600px">
    <h3 class="serif">BRIDAL APPOINTMENT</h3>
    <p>Your 1.5-hour bridal appointment is a personalized, semiprivate, one-on-one experience with an expert stylist who is dedicated to helping you find the one</p>
    <span class="btn">EXPLORE PACKAGE</span>
  </div>
  <div class="photo" style="left:50px;top:389px;width:499px;height:212px;background:linear-gradient(100deg,#e8e4de,#8a7666 50%,#d9d4cc)" role="img" aria-label="Consultant adjusting a bride's veil"></div>
  <div class="photo" style="left:649px;top:389px;width:501px;height:212px;background:linear-gradient(100deg,#f1efeb,#5a4a3e 45%,#ebe8e3 75%,#5f5a46)" role="img" aria-label="Stylist showing a white gown from the rack"></div>
</section>

<section class="faq">
  <h2 class="serif">FROM THE FAQs</h2>
  <ul>
    <li>Do I need an appointment?<em>+</em></li>
    <li>How long do appointments last?<em>+</em></li>
    <li>What should I bring to my appointment?<em>+</em></li>
    <li>What size are your sample gowns?<em>+</em></li>
    <li>What is the price range of your gowns?<em>+</em></li>
  </ul>
  <div class="abs more">Didn't find your answer? Read more FAQs here</div>
</section>

<section class="designers">
  <span>Verano</span>
  <span><i></i>Halden Formal</span>
  <span>Coraline NY</span>
  <span>Ashby</span>
</section>

<footer>
  <div class="foot-top">
    <a class="link">REQUEST AN APPOINTMENT</a>
    <span class="back">BACK TO TOP</span>
  </div>
  <div class="abs contact">appointments@gownparlormarlowe.com<br>(555)-014-2290</div>
  <div class="abs social">Journal &nbsp;|&nbsp; Gallery &nbsp;|&nbsp; Letters</div>
  <div class="brand footer-brand"><span class="name">The Gown Parlor</span><span class="sub">OF MARLOWE</span></div>
  <div class="abs address">418 Magnolia Row, Suite 2<br>Marlowe, SC 29000</div>
  <div class="abs hours"><b>STORE HOURS:</b><br>Sunday - Tuesday closed<br>Wednesday - Saturday 10am-6pm</div>

  <div class="photo" style="left:83px;top:3772px;width:163px;height:165px;background:linear-gradient(160deg,#e9e4de,#b49a86)" role="img" aria-label="Bride in lace gown and veil"></div>
  <div class="photo" style="left:257px;top:3772px;width:163px;height:165px;background:linear-gradient(160deg,#efe2da,#e0b3a3)" role="img" aria-label="Bride in a blush tulle ball gown"></div>
  <div class="photo" style="left:430px;top:3772px;width:163px;height:165px;background:linear-gradient(180deg,#c9cdb8,#6b6a5a 60%,#2c2a28)" role="img" aria-label="Couple walking outdoors"></div>
  <div class="photo" style="left:604px;top:3772px;width:163px;height:165px;background:linear-gradient(180deg,#9aa088,#eeece6 60%,#7c7a66)" role="img" aria-label="Bride under oak trees"></div>
  <div class="photo" style="left:780px;top:3772px;width:163px;height:165px;background:linear-gradient(160deg,#2f2c2a,#e8e5e0 55%,#4a4440)" role="img" aria-label="Bride in a doorway"></div>
  <div class="photo" style="left:951px;top:3772px;width:165px;height:165px;background:linear-gradient(160deg,#ddd7d0,#8e7c70 60%,#cfc7bd)" role="img" aria-label="Bride trying on a gown with a consultant"></div>

  <div class="bottom">
    <span style="left:83px">© 2026 TheGownParlorOfMarlowe</span>
    <span style="right:83px">Privacy Policy | Terms of Use</span>
  </div>
</footer>

</body>
</html>
```